Indie author needs a minimalist book cover

I need a book cover for my latest book on personal finance and investing. The book is called, "The Quiet Margin: Lessons on Steady Wealth, Calm Careers, and a Full Table". This is volume one of a three part series on the FI/RE movement, which stands for 'Financial Independence/Retire Early'. This book is on the foundational principles of FI/RE and details the specific steps that these 'Quiet Margin' involved in this community have done to position themselves to retire from paid work and live the life of their dreams - many only in their 20's, 30's and early 40's.

Title: The Quiet Margin
Author: RK Brenner
Volume 1: Foundations
Book dimensions: 6"x9"

Book Blurb (for back cover):

Let's face it, no one wants to be different. But sometimes following the 'normal' crowd gets you no further than that crowd.

When it comes to money, the normal crowd is your typical consumer. Deep in debt, struggling to make ends meet, but still spending money on the newest 'thing' that just came out.

But there's another group that's been forming - right on the fringes of the personal finance world. I call them The Quiet Margin. This book is about these superheroes of personal finance.

In it, you will learn:
• Who The Quiet Margin are and what is this FI/RE Movement they are apart of
• What basic strategy they use to control their money
• How they became debt-free - and how you can join them
• How to use the Tidewell Lever to help you really move the needle towards financial independence
• How to diversify your income with a side-hustle and which one to choose
• The money outlier savings plan that will allow you to reach financial independence in ten years or less

This first book in The Quiet Margin series is about building a solid foundation so you and your family can become Quiet Margin, reach financial freedom, retire early, and live a rich life.

Target Market(s)

Individuals looking to take control of their money, reach financial independence, and retire early.

Font styles to use
Sans Serif
Other font styles liked:
• Arvo

Colors

Designer to choose colors to be used in the design.

Requirements
Must have
• A minimalist design (see examples), the title of the book, my author name, and the volume number and name (see below).
• My vision for the cover is to have a way to represent an 'outlier' in a simple, minimalistic way. I'm not set on any specific design - I'm open to what the designers come up with; I don't want to hold back anyone's creativity.
• Title: The Quiet Margin
• Author: RK Brenner
• Volume 1: Foundations
• Book Blurb (for back cover):
• Let's face it, no one wants to be different. But sometimes following the 'normal' crowd gets you no further than that crowd.
• When it comes to money, the normal crowd is your typical consumer. Deep in debt, struggling to make ends meet, but still spending money on the newest 'thing' that just came out.
• But there's another group that's been forming - right on the fringes of the personal finance world. I call them The Quiet Margin. This book is about these superheroes of personal finance.
• In it, you will learn:
• • Who The Quiet Margin are and what is this FI/RE Movement they are apart of
• • What basic strategy they use to control their money
• • How they became debt-free - and how you can join them
• • How to use the Tidewell Lever to help you really move the needle towards financial independence
• • How to diversify your income with a side-hustle and which one to choose
• • The money outlier savings plan that will allow you to reach financial independence in ten years or less
• This first book in The Quiet Margin series is about building a solid foundation so you and your family can become Quiet Margin, reach financial freedom, retire early, and live a rich life.
Nice to have
• The subtitle - but only if it's not too crowded. Like I said before, I'm more interested in maintaining a minimalist aesthetic.
• The subtitle is: "Lessons on Steady Wealth, Calm Careers, And A Full Table"
Should not have
• Too many colors or objects on the cover.

```html
<!DOCTYPE html>
<html lang="en">
<head>
<meta charset="utf-8">
<title>The Quiet Margin — Book Cover</title>
<link href="https://fonts.googleapis.com/css2?family=Arvo:wght@400;700&family=Cardo&family=Cinzel:wght@400;500&family=Sorts+Mill+Goudy&display=swap" rel="stylesheet">
<style>
  :root {
    --backdrop: #e8e4df;
    --cover: #ffffff;
    --brown-light: #8b5a36;
    --brown-dark: #5a3417;
    --rule: #a47d5a;
    --art-top: #d9d9d9;
    --art-bottom: #8e8e8e;
  }
  * { margin: 0; padding: 0; box-sizing: border-box; }
  html, body {
    width: 1200px; height: 1200px; overflow: hidden;
    background: var(--backdrop);
  }
  .cover {
    position: absolute; left: 220px; top: 30px;
    width: 760px; height: 1140px;
    background: var(--cover);
    box-shadow: 0 8px 30px rgba(0,0,0,0.12);
  }
  .volume {
    position: absolute; top: 78px; left: 0; right: 0;
    text-align: center;
    font-family: "Cardo", serif;
    font-size: 23px; letter-spacing: 7px; line-height: 1;
    color: var(--brown-light);
  }
  .cover-art {
    position: absolute; top: 132px; left: 135px;
    width: 490px; height: 256px;
    border-radius: 6px;
    background: linear-gradient(180deg, var(--art-top), var(--art-bottom));
  }
  .title-block {
    position: absolute; top: 0; left: 95px; width: 570px;
    font-weight: 400; font-size: 16px;
    text-align: center;
  }
  .title-block > span {
    position: absolute; left: 0; right: 0; display: block;
    font-family: "Arvo", serif; line-height: 1;
  }
  .title-the {
    top: 462px;
    display: flex !important; align-items: center; gap: 24px;
    font-size: 46px; font-weight: 400;
    color: var(--brown-light);
  }
  .title-the::before, .title-the::after {
    content: ""; flex: 1; height: 4px; background: var(--rule);
  }
  .title-main {
    top: 512px;
    font-size: 112px; font-weight: 400;
    letter-spacing: 30px; padding-left: 30px;
    color: var(--brown-light);
  }
  .title-sub {
    top: 606px;
    font-size: 104px; font-weight: 700;
    letter-spacing: 4px; padding-left: 4px;
    color: var(--brown-dark);
  }
  .title-rule {
    top: 708px; height: 4px; background: var(--rule);
  }
  .subtitle {
    position: absolute; top: 728px; left: 0; right: 0;
    text-align: center;
    font-family: "Sorts Mill Goudy", serif;
    font-size: 32px; line-height: 1.4;
    color: var(--brown-light);
  }
  .author {
    position: absolute; top: 1008px; left: 0; right: 0;
    text-align: center;
    font-family: "Cinzel", serif; font-weight: 500;
    font-size: 44px; letter-spacing: 14px; line-height: 1;
    color: var(--brown-dark);
  }
</style>
</head>
<body>
  <main class="cover">
    <p class="volume">Volume 1: Foundations</p>
    <div class="cover-art" role="img" aria-label="Illustration of a row of grey game pawns with a single red pawn standing out in front"></div>
    <h1 class="title-block">
      <span class="title-the">THE</span>
      <span class="title-main">QUIET</span>
      <span class="title-sub">MARGIN</span>
      <span class="title-rule"></span>
    </h1>
    <p class="subtitle">Lessons on Steady Wealth, Calm Careers,<br>and a Full Table</p>
    <p class="author">RK BRENNER</p>
  </main>
</body>
</html>
```